2 Funky Pages + EASY stock logo = Construction Website

We would like a funky new website - Just 2 pages - to promote our project management company. A logo is also needed, but we'll provide a stock image which just needs a colour change a text added.

Here are the instructions:

"Fair Tally Homes"

#logo
The one I'd like is attached. Please change font and positioning of text though.

Tagline is "Don't be normal - Be clever"

#Colour combo
756897 Wood Veneer
D5D6D2 sand dollar
353C3F charcoal
962715 brick red

#Home - Page 1

Our cost-price home build service will save you thousands.
No, seriously - Here's how we do it (button)

- Pay what the home building companies do.
- FTH will manage the entire project.
- Use Keystonecraft Guaranteed builders and materials.
- Tender for the best industry rates.
- Get a full budget calculated for the build.
- Avoid inflated 'Fixed-price' builds.
See how it works (button)

Contact Us: 0800 615 278
enquire - Name, Phone, email, comment - SEND

#How it works - Page 2

Traditional fixed price contracts are popular because it means that any risk of unexpected problems is carried by the home builder, but the builder will generally load the price about 10 times above the actual risk carried.

It's like an over-priced insurance policy, on steroids.

Clever people do things differently.

Here's how a cost-price build works...

1) Tell us what you want to build. Dream home, townhouse, investment property, whatever.

2) We'll put a design together for you, or you can choose from a bunch of plans we've already got.

3) We'll give you a conservative price estimate.

4) We finish tweaking your plans, then send them out to our network of more than 200 builders, subcontractors and tradesmen.

5) We collect the quotes, pick the best prices, and finalise your budget. Now you buy us beer, cause you've finally realised how much you're saving.

6) Tell your friends how awesome we are, while we lodge your building consent application with Council.

7) We coordinate the builders and subbies (look, you're already speaking trade-talk) from start to finish. You pay the cost price on their work each month.

We're happy to talk numbers and give you an estimate.

Contact Us: 0800 615 278

Reason: I have seen some great design elements, but need them to come together in one site design. Also, there appears to be less attention paid to the second page design ('how it works') than is necessary... There is no viable contender there yet, compared with the great home page submissions. I've also added some further info to the brief, and note that many submissions have ignored the colour combo I've requested.

Industry/Entity Type

Construction

Number of Pages Required

2 page

Requirements
Must have
• Keystonecrafter logo (small)
• Colour combo described in brief.
Nice to have
• I've attached a stock image I like, but it's certainly not essential. I do like images with clear backgrounds though - they tend to produce a crisp looking site.
• There is a wider image similar to this, available on Pixel Vault, but Sketch Hive won't let me attach it.
Should not have
• Photos of cheesy American faces.

```html
<!DOCTYPE html>
<html lang="en">
<head>
<meta charset="utf-8">
<title>Fair Tally Homes</title>
<link href="https://fonts.googleapis.com/css2?family=Jost:wght@300;400;500;600&display=swap" rel="stylesheet">
<style>
:root{
  --charcoal:#353C3F;
  --header:#1f262c;
  --brick:#962715;
  --brick-bright:#d23a22;
  --veneer:#756897;
  --sand:#D5D6D2;
  --wall:#ececeb;
  --ink:#2c2f33;
  --white:#ffffff;
  --footer:#121416;
}
*{box-sizing:border-box;margin:0;padding:0}
html,body{width:1138px;height:1200px;overflow:hidden}
body{font-family:"Jost",sans-serif;color:var(--ink);background:var(--wall)}
.page{position:relative;width:1138px;height:1200px;overflow:hidden;background:var(--wall)}

.site-header{position:absolute;left:0;top:0;width:100%;height:122px;background:var(--header);z-index:3}
.brand{position:absolute;left:96px;top:14px;display:flex;align-items:center;gap:12px}
.brand-mark{width:82px;height:86px;background:var(--brick)}
.brand-name{font-size:25px;font-weight:400;color:var(--white);margin-top:40px}
.contact-bar{position:absolute;right:93px;top:16px;display:flex;align-items:center;height:33px;color:var(--white)}
.contact-bar .item{display:flex;align-items:center;gap:8px;padding:0 16px;font-size:14px}
.contact-bar .phone{font-size:17px;letter-spacing:.5px;border-right:1px solid #6b7177}
.quote-btn{display:flex;align-items:center;gap:10px;height:33px;padding:0 18px;background:var(--brick-bright);color:var(--white);font-size:16px}
.main-nav{position:absolute;right:93px;top:90px;display:flex;align-items:center}
.main-nav a{color:var(--white);text-decoration:none;font-size:15px;padding:0 36px;border-left:1px solid #6b7177;line-height:18px}
.main-nav a:first-child{border-left:none}
.main-nav a:last-child{padding-right:2px}
.main-nav a.active{color:var(--brick-bright);position:relative}
.main-nav a.active::after{content:"";position:absolute;left:36px;right:36px;bottom:-9px;height:2px;background:var(--brick-bright)}

.hero{position:absolute;left:0;top:122px;width:100%;height:569px;
  background:linear-gradient(100deg,#27282b 0%,#5a6b80 22%,#9fb8d6 40%,#c9d4de 55%,#bfc2c0 70%,#e4c23a 88%,#3a3a38 100%)}
.hero-title{position:absolute;left:0;top:375px;width:100%;text-align:center;font-size:50px;font-weight:600;color:var(--white);letter-spacing:-.5px;text-shadow:0 2px 10px rgba(0,0,0,.35)}

.cards{position:absolute;left:93px;top:617px;display:flex;gap:24px;z-index:2}
.card{width:301px;height:460px;background:var(--white);clip-path:polygon(50% 0,100% 48px,100% 100%,0 100%,0 48px);position:relative;display:flex;flex-direction:column;align-items:center}
.card-icon{margin-top:26px;width:80px;height:80px;border:3px solid #8e8e90;border-radius:50%;display:flex;align-items:center;justify-content:center}
.card-title{margin-top:14px;font-size:21px;font-weight:400;color:var(--ink)}
.card-body{width:100%;padding:16px 17px 0;font-size:15px;font-weight:300;line-height:19.5px;color:var(--ink)}
.card-body p{margin-bottom:13px}
.checklist{list-style:none}
.checklist li{position:relative;padding-left:23px;margin-bottom:13px}
.checklist li::before{content:"";position:absolute;left:2px;top:4px;width:10px;height:5px;border-left:2.5px solid var(--veneer);border-bottom:2.5px solid var(--veneer);transform:rotate(-45deg)}
.card-btn{position:absolute;top:403px;left:74px;width:149px;height:33px;display:flex;align-items:center;justify-content:center;color:var(--white);font-size:17px}
.card-btn.brick{background:var(--brick)}
.card-btn.veneer{background:var(--veneer)}

.enquiry{width:100%;padding:18px 16px 0}
.enquiry .field{width:100%;height:32px;border:1px solid #c9c9c9;margin-bottom:9px;padding:0 10px;font-size:13px;display:flex;align-items:center;color:#333}
.enquiry .field.comment{height:95px;align-items:flex-start;padding-top:9px}

.member-badge{position:absolute;left:93px;top:1090px;width:89px;height:110px;background:var(--white);padding:7px;z-index:4}
.member-badge span{display:block;width:100%;height:100%;background:#1d4a8f}

.site-footer{position:absolute;left:0;top:1151px;width:100%;height:49px;background:var(--footer);z-index:3;display:flex;align-items:center;justify-content:center}
.site-footer p{color:var(--white);font-size:13px}
.social{position:absolute;right:93px;top:12px;display:flex;gap:7px}
.social span{width:23px;height:23px;border-radius:50%;background:var(--white)}
</style>
</head>
<body>
<div class="page">

  <header class="site-header">
    <div class="brand">
      <span class="brand-mark" aria-hidden="true"></span>
      <span class="brand-name">Fair Tally Homes</span>
    </div>
    <div class="contact-bar">
      <span class="item phone">
        <svg width="16" height="16" viewBox="0 0 24 24"><path fill="#fff" d="M6.6 10.8a15.1 15.1 0 0 0 6.6 6.6l2.2-2.2a1 1 0 0 1 1-.25 11.4 11.4 0 0 0 3.6.57 1 1 0 0 1 1 1V20a1 1 0 0 1-1 1A17 17 0 0 1 3 4a1 1 0 0 1 1-1h3.5a1 1 0 0 1 1 1c0 1.25.2 2.45.57 3.57a1 1 0 0 1-.25 1z"/></svg>
        0800 615 278
      </span>
      <span class="item">
        <svg width="17" height="13" viewBox="0 0 24 18"><rect width="24" height="18" rx="2" fill="#fff"/><path d="M1 2l11 8 11-8" fill="none" stroke="#1f262c" stroke-width="2"/></svg>
        info@fairtallyhomes.co
      </span>
      <span class="quote-btn">
        <svg width="15" height="15" viewBox="0 0 24 24"><path fill="#fff" d="M3 17.3V21h3.7l11-11-3.7-3.7zM20.7 7a1 1 0 0 0 0-1.4l-2.3-2.3a1 1 0 0 0-1.4 0l-1.8 1.8 3.7 3.7z"/></svg>
        Get A Quote
      </span>
    </div>
    <nav class="main-nav">
      <a class="active" href="#">HOME</a>
      <a href="#">HOW IT WORKS</a>
      <a href="#">CONTACT US</a>
    </nav>
  </header>

  <section class="hero" role="img" aria-label="Photo of two people shaking hands in front of a building site with cranes and a yellow hard hat">
    <h1 class="hero-title">DON’T BE NORMAL - BE CLEVER</h1>
  </section>

  <main class="cards">
    <article class="card">
      <div class="card-icon">
        <svg width="50" height="42" viewBox="0 0 50 42"><path d="M30 2l13 11h-4v10H21V13h-4z" fill="var(--brick)"/><rect x="27" y="15" width="6" height="7" fill="#fff"/><path d="M2 26h8l8 4h12c2 0 2 3 0 3H20l1 1h10l13-7c3-1 4 2 2 3L32 40H12l-2-2H2z" fill="var(--brick)"/></svg>
      </div>
      <h2 class="card-title">Our Services</h2>
      <div class="card-body">
        <p>Our cost-price home build service will save you thousands.</p>
        <ul class="checklist">
          <li>Duis autem vel eum iriure dolor in</li>
          <li>Quis nostrud exerci tation ullamcorper</li>
          <li>Hendrerit in vulputate velit esse moles</li>
          <li>Duis autem vel eum iriure dolor in</li>
          <li>Quis nostrud exerci tation ullamcorper more.</li>
        </ul>
      </div>
      <span class="card-btn brick">How We Do It</span>
    </article>

    <article class="card">
      <div class="card-icon">
        <svg width="50" height="40" viewBox="0 0 50 40"><g fill="var(--veneer)"><circle cx="14" cy="20" r="10"/><circle cx="32" cy="10" r="7"/><circle cx="35" cy="30" r="9"/></g><g fill="#fff"><circle cx="14" cy="20" r="4"/><circle cx="32" cy="10" r="2.8"/><circle cx="35" cy="30" r="3.5"/></g></svg>
      </div>
      <h2 class="card-title">How It Works</h2>
      <div class="card-body">
        <ul class="checklist">
          <li>Pay what the home building companies do.</li>
          <li>FTH will manage the entire project.</li>
          <li>Use Keystonecraft Guaranteed builders &amp; materials.</li>
          <li>Tender for the best industry rates.</li>
          <li>Full budget calculated for the build.</li>
          <li>Avoid inflated ‘Fixed-price’ builds.</li>
        </ul>
      </div>
      <span class="card-btn veneer">How It Works</span>
    </article>

    <article class="card">
      <div class="card-icon">
        <svg width="50" height="40" viewBox="0 0 50 40"><rect x="22" y="4" width="24" height="17" fill="var(--veneer)"/><path d="M22 4l12 9 12-9" fill="none" stroke="#fff" stroke-width="1.6"/><path d="M8 16c-3 6 3 16 12 20l3-4-4-3-2 2c-3-2-5-6-5-9l3-1-2-5z" fill="var(--veneer)"/></svg>
      </div>
      <h2 class="card-title">Contact Us</h2>
      <form class="enquiry">
        <div class="field">Name</div>
        <div class="field">Email</div>
        <div class="field">Phone</div>
        <div class="field comment">Comment</div>
      </form>
      <span class="card-btn veneer">Submit</span>
    </article>
  </main>

  <div class="member-badge" aria-label="Registered builders association badge"><span></span></div>

  <footer class="site-footer">
    <p>Copyright © 2016 Fair Tally Homes. All Rights Reserved.</p>
    <div class="social" aria-label="Social links"><span></span><span></span><span></span><span></span></div>
  </footer>

</div>
</body>
</html>
```